Attention Getting Doorhanger Postcard Campaign offering HUGE Rebate on New Construction Homes

I am reestablishing my real estate career in the far North Dallas, TX area and want to offer a rebate on new construction homes to help get me started. I am requesting a doorhanger as my first project but would like a theme that I can carry over to other projects including postcards and other marketing items. I want it to look high end, clean, professional and classy. I am attaching a copy of a flier that I created that needs (no graphic designer here) some prettying up. But this is just to give you an idea of the type of style that is of interest to me.

Target Market(s)

Home buyers for new construction in far north dallas suburbs. Usually a move up buyer.

Industry/Entity Type

Real Estate

Colors

Designer to choose colors to be used in the design.

Requirements
Must have
• Catch phrase, draw attention, classy clean lines, current trend colors of blues and grays. My information, Harwood Fenn logo, equal housing and realtor logos. Fine Print: Not intended to solicit homes already listed for sale or buyers already in a buyers agency agreement with another brokerage. Please include offer details as listed in my flier. Again I am interested in a door hanger and the next round would be a flier or postcard.
Nice to have
• Picture of new homes that are in line with what is being built in my area. A few home builders sites: Silver Meadow, Brookvale Homes, Tenbury Homes, Calloway Homes.

```html
<!DOCTYPE html>
<html lang="en">
<head>
<meta charset="utf-8">
<title>New Construction Rebate Door Hangers</title>
<link href="https://fonts.googleapis.com/css2?family=Roboto:wght@300;400;500;700;900&family=Roboto+Condensed:wght@400;700&display=swap" rel="stylesheet">
<style>
  :root {
    --page: #ebe9e6;
    --blue: #1f5fb8;
    --blue-deep: #0c4fa8;
    --slate: #58585a;
    --gray-band: #707072;
    --paper: #ffffff;
    --ink: #222222;
    --line-blue: #1a4fa0;
    --dot: #5a5a5c;
  }
  * { box-sizing: border-box; margin: 0; padding: 0; }
  html, body { width: 1200px; height: 1156px; overflow: hidden; }
  body {
    background: var(--page);
    font-family: "Roboto", Arial, sans-serif;
    position: relative;
  }
  .hanger {
    position: absolute;
    top: 124px;
    width: 377px;
    height: 954px;
    background: var(--paper);
    overflow: hidden;
    box-shadow: 0 2px 6px rgba(0,0,0,.18);
  }
  .hanger--blue { left: 107px; --top: var(--blue); --band: var(--gray-band); --agent: var(--gray-band); }
  .hanger--slate { left: 694px; --top: var(--slate); --band: var(--blue-deep); --agent: var(--blue-deep); }

  .hanger__top { position: absolute; inset: 0 0 auto 0; height: 260px; background: var(--top); }
  .hanger__photo {
    position: absolute; left: 0; top: 240px; width: 377px; height: 228px; z-index: 1;
    background: linear-gradient(180deg, var(--top) 0%, #4a5a6a 35%, #6b5e50 60%, #3f5a2e 85%, #4f6b34 100%);
  }
  .hanger--slate .hanger__photo {
    background: linear-gradient(180deg, var(--top) 0%, #8a8782 30%, #7a6c5c 60%, #4f6b34 85%, #5f7d3c 100%);
  }
  .hanger__cutout { position: absolute; left: 0; top: 0; z-index: 2; }

  .headline {
    position: absolute; left: 58px; top: 400px; color: #fff; z-index: 3;
    font-weight: 900; line-height: 1;
  }
  .headline__awe { position: absolute; left: 0; top: 0; font-size: 48px; letter-spacing: 1px; }
  .headline__then { position: absolute; left: 116px; top: 8px; font-size: 20px; font-weight: 400; white-space: nowrap; }
  .headline__some { position: absolute; left: 118px; top: 23px; font-size: 48px; letter-spacing: 2px; }

  .offer-band {
    position: absolute; left: 0; top: 468px; width: 377px; height: 50px; z-index: 3;
    background: var(--band); color: #fff; padding: 9px 0 0 27px;
    font-size: 14px; font-weight: 300; line-height: 1.3;
  }
  .offer-band::before { content: ""; position: absolute; left: 0; right: 0; top: 0; height: 2px; background: var(--line-blue); }
  .offer-band strong { font-weight: 700; }
  .offer-band .big { font-size: 17px; font-weight: 700; }

  .benefits {
    position: absolute; left: 28px; top: 522px; width: 332px;
    list-style: none; font-family: "Roboto Condensed", Arial, sans-serif;
    font-size: 12.3px; line-height: 14.4px; color: var(--ink);
  }
  .benefits li { position: relative; padding-left: 10px; margin-bottom: 7.5px; }
  .benefits li::before {
    content: ""; position: absolute; left: 0; top: 5px; width: 5.5px; height: 5.5px;
    border-radius: 50%; background: var(--blue-deep);
  }
  .benefits li.justify { text-align: justify; }

  .info-box {
    position: absolute; top: 679px; height: 61px; background: var(--blue-deep); color: #fff;
    font-family: "Roboto Condensed", Arial, sans-serif; padding: 3px 4px;
  }
  .info-box--example { left: 24px; width: 173px; }
  .info-box--savings { left: 201px; width: 152px; padding-left: 6px; }
  .info-box h3 { font-size: 13.5px; font-weight: 700; line-height: 15px; }
  .info-box p { font-size: 9px; line-height: 13px; }
  .info-box b { font-size: 11.5px; }
  .info-box .note { font-size: 6.5px; line-height: 8px; }
  .info-box--savings p { font-size: 8.5px; line-height: 12px; font-weight: 700; }
  .info-box--savings p span { font-weight: 400; }

  .steps { position: absolute; left: 0; top: 744px; width: 377px; height: 70px; }
  .steps__title {
    position: absolute; left: 26px; top: 0; font-family: "Roboto Condensed", Arial, sans-serif;
    font-size: 14px; font-weight: 700; color: var(--blue-deep);
  }
  .steps__label {
    position: absolute; font-family: "Roboto Condensed", Arial, sans-serif;
    font-size: 9px; line-height: 11px; color: var(--ink); text-align: center; z-index: 1;
  }
  .steps__label--right { text-align: right; }
  .steps svg { position: absolute; left: 0; top: 0; }

  .agent {
    position: absolute; left: 0; top: 812px; width: 377px; height: 86px;
    background: var(--agent); color: #fff;
    border-top: 2px solid var(--line-blue);
  }
  .agent__intro { position: absolute; left: 35px; top: 4px; width: 226px; font-size: 7.5px; line-height: 10px; font-weight: 300; }
  .agent__intro b { font-weight: 700; }
  .agent__name { position: absolute; left: 35px; top: 32px; font-size: 24px; font-weight: 300; line-height: 1; }
  .agent__cred { position: absolute; left: 35px; top: 62px; font-size: 8.5px; line-height: 10px; }
  .agent__contact { position: absolute; left: 35px; top: 73px; font-size: 8.5px; line-height: 10px; font-weight: 700; }
  .agent__portrait {
    position: absolute; left: 275px; top: 3px; width: 66px; height: 79px;
    background: linear-gradient(160deg, #7a4a34 0%, #b07a5c 50%, #2c3a5a 100%);
  }

  .fine {
    position: absolute; left: 0; top: 898px; width: 377px; height: 56px;
    background: linear-gradient(180deg, #cfcfcf, #e6e6e6);
  }
  .fine__brand {
    position: absolute; left: 40px; top: 20px; font-size: 10px; font-weight: 500;
    color: var(--gray-band); letter-spacing: .5px;
  }
  .fine__text { position: absolute; left: 122px; top: 5px; width: 212px; font-size: 5.5px; line-height: 7px; color: #555; }
  .fine__office { position: absolute; left: 122px; top: 29px; font-family: "Roboto Condensed", Arial, sans-serif; font-size: 9.5px; font-weight: 700; color: var(--ink); }
  .hanger--slate .fine__office { color: var(--blue-deep); }
</style>
</head>
<body>

<div class="hanger hanger--blue">
  <div class="hanger__top"></div>
  <div class="hanger__photo" role="img" aria-label="Photo of a large brick new-construction home at dusk with landscaped front yard"></div>
  <svg class="hanger__cutout" width="377" height="260" viewBox="0 0 377 260">
    <rect x="0" y="146" width="130" height="14" fill="var(--page)"/>
    <circle cx="188" cy="152" r="73" fill="var(--page)"/>
    <circle cx="188" cy="152" r="95" fill="none" stroke="#fff" stroke-width="1.5" stroke-dasharray="5 4"/>
  </svg>
  <div class="headline">
    <span class="headline__awe">AWE</span>
    <span class="headline__then">and then</span>
    <span class="headline__some">SOME</span>
  </div>
  <div class="offer-band">receive A minimum of <span class="big">2.5%</span> or more to put towards<br>your <strong>NEW CONSTRUCTION</strong> home!</div>
  <ul class="benefits">
    <li>We work with 100's of builders in the local area so you are not limited to a few "select" builders.</li>
    <li>Home builders have the same bottom line sales price whether you have a REALTOR® representing you or not.</li>
    <li class="justify">Rebate program will not affect the price you pay for your home. Brokerage fees are paid through a separate marketing fund, not from the sales price of your home.</li>
    <li>Rebate program is in ADDITION to any builder or lender<br>incentives.</li>
  </ul>
  <div class="info-box info-box--example">
    <h3>For Example:</h3>
    <p><b>$400,000</b> equals a <b>$10,000</b> rebate!</p>
    <p><b>$500,000</b> equals a <b>$12,500</b> rebate!</p>
    <p class="note">*Lender approval required.</p>
  </div>
  <div class="info-box info-box--savings">
    <h3>Maximize Your Savings!</h3>
    <p><span>My Buy &amp; List package offers a</span><br><b>FLAT FEE</b> on the sale of your<br>current home. Saving you</p>
  </div>
  <div class="steps">
    <svg width="377" height="70" viewBox="0 0 377 70">
      <path d="M24 60 C60 40 80 28 100 36 C112 42 112 52 122 50 C150 44 165 20 180 30 C188 36 190 42 205 36 C230 26 248 14 262 24 C272 32 270 52 285 50 C310 46 330 42 348 38" fill="none" stroke="var(--line-blue)" stroke-width="2"/>
      <circle cx="124" cy="50" r="5" fill="var(--dot)"/>
      <circle cx="206" cy="35" r="5" fill="var(--dot)"/>
      <circle cx="285" cy="50" r="5" fill="var(--dot)"/>
      <circle cx="348" cy="38" r="5" fill="var(--dot)"/>
    </svg>
    <div class="steps__title">How it works:</div>
    <div class="steps__label" style="left:92px;top:17px;">Contact Marla<br>to register</div>
    <div class="steps__label" style="left:185px;top:6px;">Find your<br>New Home</div>
    <div class="steps__label steps__label--right" style="left:278px;top:7px;">Close &amp; Receive<br>your <b>REBATE!</b></div>
    <div class="steps__label" style="left:247px;top:58px;">Sign your Contract</div>
  </div>
  <div class="agent">
    <p class="agent__intro">I've sold hundreds of homes in the North Dallas area over the last 13 years, specializing in new construction homes. I would love to help you make your new home dreams a reality. <b>Marla</b></p>
    <div class="agent__name">Marla Prescott</div>
    <div class="agent__cred">REALTOR®, CRS, ABR, CNHS, CHMS</div>
    <div class="agent__contact">Mobile: 469.555.0187 | Email: marlaprescott@mailbox.com</div>
    <div class="agent__portrait" role="img" aria-label="Portrait photo of the agent"></div>
  </div>
  <div class="fine">
    <div class="fine__brand">Harwood Fenn</div>
    <p class="fine__text">Not intended to solicit clients in a buyer agency agreement with other brokers or for properties that may already be listed for sale. Lender authorization required for rebates. Rebates do not apply on the purchase of a preowned home.</p>
    <div class="fine__office">Each Office Is Independently Owned &amp; Operated</div>
  </div>
</div>

<div class="hanger hanger--slate">
  <div class="hanger__top"></div>
  <div class="hanger__photo" role="img" aria-label="Photo of a two-story stone and brick new-construction home at sunset with front lawn"></div>
  <svg class="hanger__cutout" width="377" height="260" viewBox="0 0 377 260">
    <rect x="0" y="146" width="130" height="14" fill="var(--page)"/>
    <circle cx="188" cy="152" r="73" fill="var(--page)"/>
    <circle cx="188" cy="152" r="95" fill="none" stroke="#fff" stroke-width="1.5" stroke-dasharray="5 4"/>
  </svg>
  <div class="headline">
    <span class="headline__awe">AWE</span>
    <span class="headline__then">and then</span>
    <span class="headline__some">SOME</span>
  </div>
  <div class="offer-band">receive A minimum of <span class="big">2.5%</span> or more to put towards<br>your <strong>NEW CONSTRUCTION</strong> home!</div>
  <ul class="benefits">
    <li>We work with 100's of builders in the local area so you are not limited to a few "select" builders.</li>
    <li>Home builders have the same bottom line sales price whether you have a REALTOR® representing you or not.</li>
    <li class="justify">Rebate program will not affect the price you pay for your home. Brokerage fees are paid through a separate marketing fund, not from the sales price of your home.</li>
    <li>Rebate program is in ADDITION to any builder or lender<br>incentives.</li>
  </ul>
  <div class="info-box info-box--example">
    <h3>For Example:</h3>
    <p><b>$400,000</b> equals a <b>$10,000</b> rebate!</p>
    <p><b>$500,000</b> equals a <b>$12,500</b> rebate!</p>
    <p class="note">*Lender approval required.</p>
  </div>
  <div class="info-box info-box--savings">
    <h3>Maximize Your Savings!</h3>
    <p><span>My Buy &amp; List package offers a</span><br><b>FLAT FEE</b> on the sale of your<br>current home. Saving you</p>
  </div>
  <div class="steps">
    <svg width="377" height="70" viewBox="0 0 377 70">
      <path d="M24 60 C60 40 80 28 100 36 C112 42 112 52 122 50 C150 44 165 20 180 30 C188 36 190 42 205 36 C230 26 248 14 262 24 C272 32 270 52 285 50 C310 46 330 42 348 38" fill="none" stroke="var(--line-blue)" stroke-width="2"/>
      <circle cx="124" cy="50" r="5" fill="var(--dot)"/>
      <circle cx="206" cy="35" r="5" fill="var(--dot)"/>
      <circle cx="285" cy="50" r="5" fill="var(--dot)"/>
      <circle cx="348" cy="38" r="5" fill="var(--dot)"/>
    </svg>
    <div class="steps__title">How it works:</div>
    <div class="steps__label" style="left:92px;top:17px;">Contact Marla<br>to register</div>
    <div class="steps__label" style="left:185px;top:6px;">Find your<br>New Home</div>
    <div class="steps__label steps__label--right" style="left:278px;top:7px;">Close &amp; Receive<br>your <b>REBATE!</b></div>
    <div class="steps__label" style="left:247px;top:58px;">Sign your Contract</div>
  </div>
  <div class="agent">
    <p class="agent__intro">I've sold hundreds of homes in the North Dallas area over the last 13 years, specializing in new construction homes. I would love to help you make your new home dreams a reality. <b>Marla</b></p>
    <div class="agent__name">Marla Prescott</div>
    <div class="agent__cred">REALTOR®, CRS, ABR, CNHS, CHMS</div>
    <div class="agent__contact">Mobile: 469.555.0187 | Email: marlaprescott@mailbox.com</div>
    <div class="agent__portrait" role="img" aria-label="Portrait photo of the agent"></div>
  </div>
  <div class="fine">
    <div class="fine__brand">Harwood Fenn</div>
    <p class="fine__text">Not intended to solicit clients in a buyer agency agreement with other brokers or for properties that may already be listed for sale. Lender authorization required for rebates. Rebates do not apply on the purchase of a preowned home.</p>
    <div class="fine__office">Each Office Is Independently Owned &amp; Operated</div>
  </div>
</div>

</body>
</html>
```